RK Bastone Construction Inc.

Design a new business card for our construction company
To be removed from current card:
Delete 25 years
Delete Tenant fit up Renovations section

```html
<!DOCTYPE html>
<html lang="en">
<head>
<meta charset="utf-8">
<title>RK Bastone Construction Inc. – Business Card</title>
<link rel="stylesheet" href="https://fonts.googleapis.com/css2?family=Krona+One&family=Michroma&display=swap">
<style>
  :root {
    --purple: #55306f;
    --teal: #267a6e;
    --slate: #4a5b7a;
    --white: #ffffff;
    --backdrop: #d3d4d6;
    --gradient: linear-gradient(90deg, #54306f 0%, #57407a 20%, #4b5a7a 45%, #3f6a74 65%, #2a786e 85%, #267a6e 100%);
  }
  * { box-sizing: border-box; margin: 0; padding: 0; }
  html, body { width: 900px; height: 1200px; overflow: hidden; }
  body {
    background: var(--backdrop);
    position: relative;
    font-family: "Michroma", "Arial", sans-serif;
  }
  .card {
    position: absolute;
    left: 120px;
    width: 660px;
    height: 379px;
    overflow: hidden;
  }
  .card--front { top: 202px; background: var(--gradient); color: var(--white); }
  .card--back { top: 619px; background: var(--white); }

  .wordmark {
    position: absolute;
    left: 0; right: 0;
    text-align: center;
    font-family: "Krona One", "Arial Black", sans-serif;
    line-height: 1;
  }
  .wordmark__name { display: block; font-size: 38px; letter-spacing: 1px; }
  .wordmark__suffix { display: block; font-size: 18px; letter-spacing: 4px; margin-top: 10px; }
  .card--front .wordmark { top: 150px; color: var(--white); }
  .card--back .wordmark { top: 47px; color: var(--purple); }

  .services {
    position: absolute;
    left: 0; right: 0; top: 329px;
    text-align: center;
    font-family: "Krona One", "Arial Black", sans-serif;
    font-size: 14px;
    letter-spacing: 1.5px;
  }

  .person {
    position: absolute;
    left: 0; right: 0; top: 176px;
    text-align: center;
    font-family: "Krona One", "Arial Black", sans-serif;
    font-size: 23px;
    letter-spacing: 1px;
  }
  .person__first { color: var(--purple); }
  .person__last { color: var(--teal); }

  .phone {
    position: absolute;
    left: 0; right: 0; top: 213px;
    text-align: center;
    color: var(--teal);
    font-size: 16px;
    letter-spacing: 3px;
  }
  .icon { display: inline-block; vertical-align: -2px; margin-right: 4px; }

  .contact-row {
    position: absolute;
    left: 0; right: 0; top: 293px;
    text-align: center;
    color: var(--purple);
    font-size: 12px;
  }
  .contact-row span + span { margin-left: 16px; }

  .address {
    position: absolute;
    left: 0; right: 0; top: 328px;
    text-align: center;
    color: var(--purple);
    font-size: 12px;
  }

  .band {
    position: absolute;
    left: 0; right: 0; bottom: 0;
    height: 13px;
    background: var(--gradient);
  }
</style>
</head>
<body>
  <section class="card card--front" aria-label="Business card front">
    <div class="wordmark">
      <span class="wordmark__name">RK BASTONE</span>
      <span class="wordmark__suffix">CONSTRUCTION INC.</span>
    </div>
    <p class="services">Office | Retail | Institutional</p>
  </section>

  <section class="card card--back" aria-label="Business card back">
    <div class="wordmark">
      <span class="wordmark__name">RK BASTONE</span>
      <span class="wordmark__suffix">CONSTRUCTION INC.</span>
    </div>
    <p class="person"><span class="person__first">Marco</span> <span class="person__last">Bastone</span></p>
    <p class="phone">
      <svg class="icon" width="15" height="15" viewBox="0 0 24 24" aria-hidden="true"><path fill="#267a6e" d="M6.6 10.8a15.2 15.2 0 0 0 6.6 6.6l2.2-2.2c.3-.3.7-.4 1-.2 1.1.4 2.3.6 3.6.6.6 0 1 .4 1 1V20c0 .6-.4 1-1 1A17 17 0 0 1 3 4c0-.6.4-1 1-1h3.5c.6 0 1 .4 1 1 0 1.3.2 2.5.6 3.6.1.3 0 .7-.2 1z"/></svg>613-555-0142
    </p>
    <p class="contact-row">
      <span><svg class="icon" width="15" height="11" viewBox="0 0 20 14" aria-hidden="true"><rect width="20" height="14" fill="#267a6e"/><path d="M0 0l10 7 10-7M0 14l7-6M20 14l-7-6" stroke="#fff" stroke-width="1.4" fill="none"/></svg>marco@rkbastoneconst.ca</span>
      <span><svg class="icon" width="14" height="14" viewBox="0 0 20 20" aria-hidden="true"><g fill="none" stroke="#267a6e" stroke-width="1.6"><circle cx="10" cy="10" r="8.5"/><ellipse cx="10" cy="10" rx="4" ry="8.5"/><path d="M1.5 10h17M3 5.5h14M3 14.5h14"/></g></svg>www.rkbastoneconst.ca</span>
    </p>
    <p class="address">2180 Meadowbrook Rd., Suite 200, Ottawa, ON K1B 4W7</p>
    <div class="band"></div>
  </section>
</body>
</html>
```